VerdaTurfix - 11" x 4" Door Hanger, full color both sides

We need a door hanger designed, 11" x 4", full color both sides, We are a lawn care company that provides lawn mowing, and other services to clients. This door hanger will be place on the 9 neighbors of our current clients. The ad needs to state that we provided lawn service to one of their neighbors today, and that we are in their neighborhood each week on that day. The door hanger will have 4 printings, substituting the day of Tuesday, Wednesday, Thursday, and Friday. All the art work and text will remain the same except the day of the week. For information about VerdaTurfix, please visit our website www.verdaturfix.net. The main emphasis of the message should be that we are their every week on that day, and the benefits to them of using our service (ie. quality time with their family, golf, sports, resting, etc., instead of mowing the lawn). At the bottom of the door hanger will be a coupon offering their tenth (10th) lawn service free, which is the same as a 10% discount.

I have uploaded a template files for the front and back of an 11 x 4 door hanger, The templates are pdf, jpeg, or eps files. The final product can be a pdf, jpeg, or eps file.

Target Market(s)

Neighbors of our existing clients

Industry/Entity Type

Lawn Care

Font styles to use
Serif

Requirements
Must have
• Professional design and art, Short conversational message that relays the following thoughts:
• 1. We mowed your neighbor's lawn today!
• 2. We are in your neighborhood every Tuesday!
• 3. Our lawn service is guaranteed.
• 4. Call to action - Call us today! 555-014-7382
• 5. Of course our contact info, name, phone number, website address.
• 6. Coupon at bottom for "10th lawn service Free!"
Nice to have
• Art work from our website is fine to use, That carries our theme throughout our campaign.
Should not have
• Very wordy. This is basically a billboard, Have very few seconds to grab their attention.

```html
<!DOCTYPE html>
<html lang="en">
<head>
<meta charset="utf-8">
<title>VerdaTurfix Door Hanger</title>
<link href="https://fonts.googleapis.com/css2?family=PT+Sans:ital,wght@0,400;0,700;1,400&family=Oswald:wght@400;500;600&display=swap" rel="stylesheet">
<style>
  :root {
    --page: #ebebe8;
    --green-deep: #0f5a24;
    --green-dark: #146b2a;
    --green-mid: #1f8a31;
    --green-lime: #7cc242;
    --yellow: #e9e52c;
    --white: #ffffff;
  }
  * { margin: 0; padding: 0; box-sizing: border-box; }
  html, body { width: 1200px; height: 1172px; overflow: hidden; background: var(--page); }
  body { position: relative; font-family: "PT Sans", sans-serif; }

  .hanger {
    position: absolute; top: 118px; width: 340px; height: 935px;
    border-radius: 14px; overflow: hidden;
    background: linear-gradient(180deg, var(--green-mid) 0%, var(--green-dark) 30%, var(--green-deep) 100%);
    box-shadow: 0 3px 10px rgba(0,0,0,.25);
  }
  .hanger--front { left: 167px; }
  .hanger--back { left: 670px; }

  .hanger__art { position: absolute; inset: 0; }

  .headline {
    position: absolute; top: 14px; left: 0; width: 100%;
    text-align: center; color: var(--white);
    font-weight: 700; font-size: 21px; line-height: 30px; letter-spacing: -0.2px;
    white-space: nowrap;
  }

  .brand {
    position: absolute; left: 0; width: 100%; top: 518px;
    text-align: center; color: var(--white);
    font-weight: 700; font-size: 40px; letter-spacing: 2px;
    text-shadow: 0 2px 3px rgba(0,0,0,.35);
    white-space: nowrap;
  }

  .tagline {
    position: absolute; top: 572px; left: 0; width: 100%;
    text-align: center; color: var(--yellow);
    font-style: italic; font-size: 21px; line-height: 28px;
  }
  .guarantee {
    position: absolute; top: 633px; left: 0; width: 100%;
    text-align: center; color: var(--white); font-size: 15px;
  }

  .services {
    position: absolute; top: 582px; left: 10px; right: 6px; list-style: none;
    color: var(--green-lime); font-size: 17.5px; line-height: 24px;
  }
  .services li { display: flex; align-items: center; gap: 8px; white-space: nowrap; }
  .services svg { width: 12px; height: 10px; flex: none; }

  .coupon {
    position: absolute; left: 10px; width: 320px; height: 112px;
    border: 2px solid var(--green-lime); border-radius: 8px; overflow: hidden;
    background: linear-gradient(180deg, #a9d46a 0%, #6fb23d 45%, #3d8d27 75%, #2c7420 100%);
  }
  .hanger--front .coupon { top: 679px; }
  .hanger--back .coupon { top: 719px; }
  .coupon__number {
    position: absolute; left: 20px; top: 4px;
    font-family: "Oswald", sans-serif; font-weight: 600;
    font-size: 86px; line-height: 100px; color: var(--white);
    text-shadow: 0 2px 4px rgba(0,0,0,.35); letter-spacing: -3px;
  }
  .coupon__suffix {
    position: absolute; left: 92px; top: 50px;
    font-family: "Oswald", sans-serif; font-weight: 500;
    font-size: 46px; line-height: 56px; color: var(--white);
    text-shadow: 0 2px 4px rgba(0,0,0,.35); white-space: nowrap;
  }
  .coupon__suffix b { font-weight: 600; font-size: 54px; margin-left: 10px; }
  .coupon__label {
    position: absolute; left: 154px; top: 16px;
    font-family: "Oswald", sans-serif; font-size: 20px; color: var(--white);
    letter-spacing: 0.3px; text-shadow: 0 1px 2px rgba(0,0,0,.3); white-space: nowrap;
  }
  .coupon__ribbon {
    position: absolute; right: -34px; top: 16px; width: 130px; height: 20px;
    transform: rotate(45deg); background: var(--green-lime);
    color: var(--white); font-size: 12px; line-height: 20px; text-align: center;
    letter-spacing: 0.5px;
  }

  .cta-front {
    position: absolute; top: 804px; left: 0; width: 100%; text-align: center;
    font-family: "Oswald", sans-serif; color: var(--yellow); font-size: 25px;
  }
  .phone-front {
    position: absolute; top: 838px; left: 0; width: 100%; text-align: center;
    font-family: "Oswald", sans-serif; font-weight: 500; color: var(--white);
    font-size: 46px; letter-spacing: 1px; text-shadow: 0 2px 3px rgba(0,0,0,.35);
    white-space: nowrap;
  }
  .cta-back {
    position: absolute; top: 850px; left: 10px; right: 10px; height: 48px;
    display: flex; align-items: baseline; justify-content: center; gap: 12px;
    font-family: "Oswald", sans-serif; white-space: nowrap;
  }
  .cta-back__label { color: var(--yellow); font-size: 17px; letter-spacing: -0.3px; }
  .cta-back__phone {
    color: var(--white); font-weight: 500; font-size: 33px; letter-spacing: 0.5px;
    text-shadow: 0 2px 3px rgba(0,0,0,.35);
  }

  .web {
    position: absolute; bottom: 0; left: 0; width: 100%; height: 30px;
    background: var(--white); text-align: center;
    color: var(--green-deep); font-weight: 700; font-size: 20px; line-height: 30px;
  }
</style>
</head>
<body>

<section class="hanger hanger--front">
  <svg class="hanger__art" width="340" height="935" viewBox="0 0 340 935">
    <defs>
      <linearGradient id="lawnFront" x1="0" y1="0" x2="1" y2="1">
        <stop offset="0" stop-color="#7fbb48"/>
        <stop offset="1" stop-color="#3f7f2a"/>
      </linearGradient>
      <linearGradient id="yardFront" x1="0" y1="0" x2="0" y2="1">
        <stop offset="0" stop-color="#c9c6b8"/>
        <stop offset=".45" stop-color="#8fb35a"/>
        <stop offset="1" stop-color="#69b53a"/>
      </linearGradient>
    </defs>
    <path d="M0 215 Q110 118 340 108 L340 126 Q130 130 0 238 Z" fill="var(--green-lime)"/>
    <path role="img" aria-label="Photo of a lawn mower cutting green grass" d="M0 238 Q130 130 340 126 L340 482 Q170 480 0 495 Z" fill="url(#lawnFront)"/>
    <path d="M0 495 Q170 480 340 482" stroke="var(--green-lime)" stroke-width="5" fill="none"/>
    <circle cx="245" cy="412" r="94" fill="var(--green-deep)"/>
    <circle role="img" aria-label="Photo of a house with a front garden and lawn" cx="245" cy="412" r="86" fill="url(#yardFront)" stroke="var(--white)" stroke-width="3"/>
    <circle cx="170" cy="139" r="56" fill="var(--page)" stroke="var(--green-deep)" stroke-width="4"/>
  </svg>

  <h2 class="headline">WE MOWED YOURNEIGHBOR'S<br>LAWN TODAY!</h2>
  <h1 class="brand">VERDATURFIX</h1>
  <p class="tagline">We are in your<br>neighborhood every Tuesday!</p>
  <p class="guarantee">Our lawn service is guaranteed.</p>

  <div class="coupon">
    <span class="coupon__number">10</span>
    <span class="coupon__suffix">TH<b>FREE!</b></span>
    <span class="coupon__label">LAWN SERVICE</span>
    <span class="coupon__ribbon">DISCOUNT</span>
  </div>

  <p class="cta-front">CALL US TODAY!</p>
  <p class="phone-front">555-014-7382</p>
  <p class="web">www.verdaturfix.net</p>
</section>

<section class="hanger hanger--back">
  <svg class="hanger__art" width="340" height="935" viewBox="0 0 340 935">
    <defs>
      <linearGradient id="gardenBack" x1="0" y1="0" x2="0" y2="1">
        <stop offset="0" stop-color="#3c4a4a"/>
        <stop offset=".3" stop-color="#8a5a4a"/>
        <stop offset=".45" stop-color="#7cbf3e"/>
        <stop offset="1" stop-color="#5aa832"/>
      </linearGradient>
      <linearGradient id="handBack" x1="0" y1="0" x2="0" y2="1">
        <stop offset="0" stop-color="#9fcf6a"/>
        <stop offset="1" stop-color="#3f8f2a"/>
      </linearGradient>
    </defs>
    <path d="M0 215 Q110 118 340 108 L340 126 Q130 130 0 238 Z" fill="var(--green-lime)"/>
    <path role="img" aria-label="Photo of a front yard with flower beds and a green lawn" d="M0 238 Q130 130 340 126 L340 490 Q170 486 0 495 Z" fill="url(#gardenBack)"/>
    <path d="M0 495 Q170 486 340 490" stroke="var(--green-lime)" stroke-width="5" fill="none"/>
    <circle cx="258" cy="428" r="82" fill="var(--green-deep)"/>
    <circle role="img" aria-label="Photo of a hand resting on freshly cut grass" cx="258" cy="428" r="74" fill="url(#handBack)" stroke="var(--white)" stroke-width="3"/>
    <circle cx="170" cy="139" r="56" fill="var(--page)" stroke="var(--green-deep)" stroke-width="4"/>
  </svg>

  <h2 class="headline">WE MOWED YOURNEIGHBOR'S<br>LAWN TODAY!</h2>
  <h1 class="brand">VERDATURFIX</h1>

  <ul class="services">
    <li><svg viewBox="0 0 12 10"><path d="M1 5 L4.5 8.5 L11 1.5" stroke="var(--green-lime)" stroke-width="2" fill="none"/></svg>Weekly or bi-weekly lawn mowing</li>
    <li><svg viewBox="0 0 12 10"><path d="M1 5 L4.5 8.5 L11 1.5" stroke="var(--green-lime)" stroke-width="2" fill="none"/></svg>Fertilization &amp; weed-control programs</li>
    <li><svg viewBox="0 0 12 10"><path d="M1 5 L4.5 8.5 L11 1.5" stroke="var(--green-lime)" stroke-width="2" fill="none"/></svg>Landscape services</li>
    <li><svg viewBox="0 0 12 10"><path d="M1 5 L4.5 8.5 L11 1.5" stroke="var(--green-lime)" stroke-width="2" fill="none"/></svg>Sprinkler repair</li>
    <li><svg viewBox="0 0 12 10"><path d="M1 5 L4.5 8.5 L11 1.5" stroke="var(--green-lime)" stroke-width="2" fill="none"/></svg>Landscape lighting</li>
  </ul>

  <div class="coupon">
    <span class="coupon__number">10</span>
    <span class="coupon__suffix">TH<b>FREE!</b></span>
    <span class="coupon__label">LAWN SERVICE</span>
    <span class="coupon__ribbon">DISCOUNT</span>
  </div>

  <p class="cta-back"><span class="cta-back__label">CALL US TODAY!</span><span class="cta-back__phone">555-014-7382</span></p>
  <p class="web">www.verdaturfix.net</p>
</section>

</body>
</html>
```